Electronics Recycling and IT Asset Disposition Flyer and Brochure Design

We need a 2 side A5 Flyer and 4 side A4 folder( brochure) for our electronics waste recycling and IT asset management and disposition business.
Our business provides free electronics waste recycling for companies, schools, learning institutions,councils, IT companies and government sectors. Many people are ignorant of responsible recycling of electronics which could harm our health if not treated properly.
The list of other services attached in the pdf.
We provide an end to end and tailored solution for our customers from collection, logistics, data sanitisation, remarketing and recycling.

The Flyer should create awareness of responsible electronics recycling and drive the audience to contact us or go to our website to learn more about the company and services.A brief list of services should also be included in the flyer.The goal is to get the audience to contact us to enquire more about our services.

The Brochure should include all the above plus provide more details about the company, processes, services,contact details (fb, linkedin,Twitter). The goal is to convert the audience to customers for recycling and provide other services as added services.

The final design for both flyer and brochure should communicate responsible recycling of electronic scrap and tailored solution for every organisation.

The company website is www.kelvora-scrap.com.au based in Australia. We serve clients nationwide.

Target Market(s)

IT companies, Corporate, schools and learning institutions, government sector

Industry/Entity Type

Recycling

Contact Information for Business Card

Name: Darren Okefield
email: darren@kelvora-scrap.com.au
website: www.kelvora-scrap.com.au
mobile: +614 173 60294
Phone: 1300 46 2587

Font styles to use
Serif

Requirements
Must have
• I would like the designs to have more images and icons
Nice to have
Should not have
• none

```html
<!DOCTYPE html>
<html lang="en">
<head>
<meta charset="utf-8">
<title>Kelvora Scrap – Folder Spread</title>
<link href="https://fonts.googleapis.com/css2?family=Jost:wght@400;500;600;700&family=Oswald:wght@600;700&display=swap" rel="stylesheet">
<style>
  :root{
    --bg:#3a3a3a;
    --paper:#f3f4f3;
    --green:#6aa54a;
    --green-dark:#3f7d35;
    --green-light:#8cc063;
    --grey:#5f6062;
    --bar:#2b2b2b;
    --ink:#1c1c1c;
    --text:#444;
    --white:#ffffff;
  }
  *{margin:0;padding:0;box-sizing:border-box}
  html,body{width:1200px;height:789px;overflow:hidden;background:var(--bg)}
  .spread{position:absolute;left:80px;top:27px;width:1040px;height:735px;background:var(--paper);font-family:"Jost",sans-serif;color:var(--text);overflow:hidden;box-shadow:0 10px 30px rgba(0,0,0,.4)}
  .spread-shapes{position:absolute;inset:0}
  .fold{position:absolute;left:520px;top:0;width:1px;height:100%;background:rgba(0,0,0,.08)}

  /* back cover */
  .testimonials{position:absolute;left:42px;top:48px;width:350px;z-index:2}
  .testimonials__rule{width:46px;height:5px;background:var(--green);margin-bottom:8px}
  .testimonials__title{font-size:19px;font-weight:500;color:#333;letter-spacing:.5px;margin-bottom:22px}
  .quote{position:relative;padding-left:4px;margin-bottom:30px}
  .quote__mark{position:absolute;font-family:Georgia,serif;font-size:34px;color:#bbb;line-height:1}
  .quote__mark--open{left:0;top:-26px}
  .quote__mark--close{right:0;top:-6px}
  .quote__text{font-size:11px;line-height:1.45;color:#555;padding-top:12px;width:320px}
  .quote__author{text-align:right;padding-right:30px;font-size:10px;line-height:1.3;color:#555;margin-top:4px}
  .quote__role{font-size:9px}

  .back-brand{position:absolute;left:34px;top:498px;font-size:26px;font-weight:700;color:var(--white);letter-spacing:.5px}
  .locations{position:absolute;left:34px;top:548px;color:var(--white);font-size:12px;line-height:1.35}
  .location{display:flex;gap:10px;margin-bottom:12px}
  .location svg{flex:none;margin-top:2px}
  .location__city{font-weight:600}
  .contact-email{display:flex;align-items:center;gap:10px;position:absolute;left:34px;top:652px;color:var(--white);font-size:12px}
  .follow{position:absolute;left:330px;top:652px;display:flex;align-items:center;gap:6px;color:var(--white);font-size:10px}
  .follow__dot{width:16px;height:16px;border-radius:50%;background:var(--green-light)}
  .call-bar{position:absolute;left:34px;top:700px;display:flex;align-items:center;gap:8px;color:var(--white);font-size:14px;font-weight:700;letter-spacing:.5px}

  /* front cover */
  .front-brand{position:absolute;right:48px;top:44px;font-size:30px;font-weight:700;color:var(--green-dark);letter-spacing:.5px}
  .hero-art{position:absolute;left:415px;top:190px;width:250px;height:250px;border-radius:50%;background:radial-gradient(circle at 50% 50%,#5c6a72 0 48%,#6aa54a 49% 100%)}
  .headline{position:absolute;right:40px;top:420px;text-align:right;text-transform:uppercase;line-height:1}
  .headline span{display:block}
  .headline__dark{font-family:"Oswald",sans-serif;font-weight:700;color:var(--ink);font-size:30px;letter-spacing:.5px}
  .headline__green{font-family:"Oswald",sans-serif;font-weight:700;color:var(--green-dark);font-size:38px;letter-spacing:1px}
  .headline__green--big{font-size:44px}
  .website{position:absolute;right:44px;top:634px;display:flex;align-items:center;gap:8px;color:var(--white);font-size:14px;font-weight:500;line-height:16px;white-space:nowrap;transform:rotate(-17deg);transform-origin:right center}
</style>
</head>
<body>
<main class="spread">
  <svg class="spread-shapes" width="1040" height="735" viewBox="0 0 1040 735" aria-hidden="true">
    <defs>
      <linearGradient id="circuit" x1="0" y1="0" x2="1" y2="1">
        <stop offset="0" stop-color="#d9ddd8"/>
        <stop offset="1" stop-color="#c6cdc4"/>
      </linearGradient>
    </defs>
    <polygon points="400,360 520,40 800,260 760,520 520,640 400,560" fill="url(#circuit)" opacity=".8"/>
    <polygon points="0,380 330,450 0,470" fill="var(--green-dark)"/>
    <polygon points="0,470 130,530 0,590" fill="var(--grey)"/>
    <polygon points="0,590 130,530 500,470 520,735 0,735" fill="var(--green)"/>
    <polygon points="0,690 460,690 520,650 520,735 0,735" fill="var(--bar)"/>
    <polygon points="1040,150 870,330 1040,360" fill="var(--green)"/>
    <polygon points="860,340 990,340 920,260" fill="var(--green-dark)"/>
    <polygon points="600,735 1040,600 1040,650 760,735" fill="var(--green)"/>
  </svg>
  <div class="fold"></div>

  <section class="testimonials">
    <div class="testimonials__rule"></div>
    <h2 class="testimonials__title">TESTIMONIALS</h2>
    <blockquote class="quote">
      <span class="quote__mark quote__mark--open">“</span>
      <p class="quote__text">Kelvora Scrap helped us to remove all our old equipment from our IT store room on a very short notice. Will be using their services again.</p>
      <p class="quote__author">Marcus Elridge<br><span class="quote__role">IT Infrastructure Manager</span></p>
      <span class="quote__mark quote__mark--close">”</span>
    </blockquote>
    <blockquote class="quote">
      <span class="quote__mark quote__mark--open">“</span>
      <p class="quote__text">I highly recommend them for their professionalism and response time. They delivered a mammoth task of relocating our IT room without a hiccup. Thanks Kelvora Team</p>
      <p class="quote__author">Priya Santorin<br><span class="quote__role">IT Services Manager</span></p>
      <span class="quote__mark quote__mark--close">”</span>
    </blockquote>
  </section>

  <div class="back-brand">Kelvora Scrap</div>
  <div class="locations">
    <div class="location">
      <svg width="12" height="16" viewBox="0 0 12 16"><path d="M6 0a6 6 0 0 1 6 6c0 4-6 10-6 10S0 10 0 6a6 6 0 0 1 6-6z" fill="#fff"/><circle cx="6" cy="6" r="2.2" fill="var(--green)"/></svg>
      <div><span class="location__city">Sydney</span><br>41-43 Carrow Road,<br>Kellyville 2155 NSW</div>
    </div>
    <div class="location">
      <svg width="12" height="16" viewBox="0 0 12 16"><path d="M6 0a6 6 0 0 1 6 6c0 4-6 10-6 10S0 10 0 6a6 6 0 0 1 6-6z" fill="#fff"/><circle cx="6" cy="6" r="2.2" fill="var(--green)"/></svg>
      <div><span class="location__city">Melbourne</span><br>22 Farlow Street, Braybrook 3019 VIC</div>
    </div>
  </div>
  <div class="contact-email">
    <svg width="14" height="10" viewBox="0 0 14 10"><rect x=".5" y=".5" width="13" height="9" fill="none" stroke="#fff"/><path d="M.5 .5 7 6l6.5-5.5" fill="none" stroke="#fff"/></svg>
    contact@kelvora-scrap.com.au
  </div>
  <div class="follow">Follow Us: <span class="follow__dot"></span><span class="follow__dot"></span><span class="follow__dot"></span></div>
  <div class="call-bar">
    <svg width="14" height="14" viewBox="0 0 14 14"><circle cx="7" cy="7" r="6.3" fill="none" stroke="#fff" stroke-width="1.2"/><path d="M4.5 4c.5 2.5 2.5 4.8 5 5.5l.8-1.2-1.5-.8-.6.6C7 7.5 6.3 6.7 5.9 5.5l.6-.6-.8-1.5z" fill="#fff"/></svg>
    CALL NOW 1300 46 2587
  </div>

  <div class="front-brand">Kelvora Scrap</div>
  <div class="hero-art" role="img" aria-label="Green recycling arrows circling a laptop, desktop monitor and tablet"></div>
  <h1 class="headline">
    <span class="headline__dark">Be Responsible</span>
    <span class="headline__green">Today for a</span>
    <span class="headline__dark">Better Future</span>
    <span class="headline__green headline__green--big">Tomorrow</span>
  </h1>
  <div class="website">
    <svg width="13" height="13" viewBox="0 0 13 13"><circle cx="6.5" cy="6.5" r="6" fill="none" stroke="#fff"/><ellipse cx="6.5" cy="6.5" rx="2.6" ry="6" fill="none" stroke="#fff"/><path d="M.5 6.5h12" stroke="#fff"/></svg>
    www.kelvora-scrap.com.au
  </div>
</main>
</body>
</html>
```